Violet Harbor Spa - New services (Slimming Massage)

To create an striking image that create an appetite for slimming massage. This is a new service by Violet Harbor Spa. Firstly, new Harbor Spa stands for slimming, massage and meditation for both man and woman. The company use to focus only on massage and meditation but now we are expanding our scope of our business. Please visit www.violetharborspa.example. The impact created must tell a story how by using the Violet Harbor Spa massage services, the beautiful lady and man will be slim instead of fat. The price for the massage is $88 net price only.

The message about poster should be somewhat like this.

"Are you trouble by being out of shape and wanting to get back into the shape quickly? Come and try our slimming massage only at $88 dollar, results guarantee (Terms and conditions applied).

Target Market(s)

Niche and high call

Industry/Entity Type

Massage

Requirements
Must have
• black color background
• logo
• company address
• telephone number must be big
• www.facebook/violetharborspa
• Beautiful image
• Natural, can use tree or lotus as recommendation
• Unisex photo instead of woman only
• Shapely woman and man who become very good shape after massage

```html
<!DOCTYPE html>
<html lang="en">
<head>
<meta charset="utf-8">
<title>Violet Harbor Spa – Slimming Massage</title>
<link rel="stylesheet" href="https://fonts.googleapis.com/css2?family=Cinzel:wght@400&family=Arimo:wght@400&display=swap">
<style>
  :root {
    --stage: #7b7b7b;
    --black: #000000;
    --green: #8dc63f;
    --blue: #4aa3df;
    --white: #ffffff;
    --panel: #ffffff;
    --serif: "Cinzel", "Times New Roman", serif;
    --sans: "Arimo", Arial, sans-serif;
  }
  * { margin: 0; padding: 0; box-sizing: border-box; }
  html, body {
    width: 1200px; height: 900px; overflow: hidden;
    background: var(--stage);
  }
  .banner {
    position: absolute; left: 53px; top: 178px;
    width: 1096px; height: 548px;
    background: var(--black);
    overflow: hidden;
  }
  .mist {
    position: absolute; left: -120px; top: 250px; width: 1000px; height: 420px;
    background: radial-gradient(closest-side, rgba(55,120,130,.5) 0%, rgba(30,70,80,.28) 45%, rgba(0,0,0,0) 100%);
  }
  .feather {
    position: absolute; left: 112px; top: 100px; width: 180px; height: 70px;
    transform: rotate(-28deg);
    background: radial-gradient(closest-side, rgba(235,242,255,.95) 0%, rgba(170,190,220,.55) 40%, rgba(0,0,0,0) 100%);
  }
  .stones {
    position: absolute; left: 10px; top: 355px; width: 140px; height: 170px;
    background: radial-gradient(closest-side, #56666a 0%, #34413f 45%, rgba(20,40,45,.4) 75%, rgba(0,0,0,0) 100%);
  }
  .lotus {
    position: absolute; left: 85px; top: 410px; width: 170px; height: 125px;
    background: radial-gradient(closest-side, rgba(225,200,255,.95) 0%, rgba(140,130,240,.6) 40%, rgba(60,80,160,.2) 75%, rgba(0,0,0,0) 100%);
  }
  .headline {
    position: absolute; left: 190px; width: 700px; top: 0; height: 290px;
    text-align: center; font-family: var(--serif);
    color: var(--white); line-height: 1;
  }
  .headline p {
    position: absolute; left: 0; right: 0;
    display: flex; align-items: baseline; justify-content: center; gap: 7px; white-space: nowrap;
  }
  .headline .l1 { top: 76px; }
  .headline .l2 { top: 101px; }
  .headline .l3 { top: 139px; }
  .headline .l4 { top: 179px; }
  .headline .l5 { top: 208px; }
  .headline .l6 { top: 254px; }
  .headline .s { font-size: 13px; }
  .headline .g { color: var(--green); font-size: 21px; }
  .headline .b { color: var(--blue); font-size: 29px; }
  .headline .bm { color: var(--blue); font-size: 21px; }
  .headline .gl { color: var(--green); font-size: 31px; }
  .headline .price { color: var(--green); font-size: 35px; }
  .headline .terms { font-size: 11px; font-style: italic; letter-spacing: .3px; }
  .contact {
    position: absolute; left: 280px; width: 510px; top: 402px;
    text-align: center; font-family: var(--sans);
  }
  .address { color: var(--green); font-size: 19px; }
  .phone { color: var(--white); font-size: 40px; margin-top: 12px; }
  .web { color: var(--green); font-size: 20px; margin-top: 10px; }
  .rule-green { position: absolute; left: 872px; top: 0; width: 3px; height: 548px; background: var(--green); }
  .rule-blue  { position: absolute; left: 877px; top: 0; width: 3px; height: 548px; background: var(--blue); }
  .side-panel {
    position: absolute; left: 880px; top: 0; width: 216px; height: 548px;
    background: var(--panel);
  }
  .brand-dot {
    position: absolute; left: 80px; top: 40px; width: 56px; height: 56px;
    border-radius: 50%; background: var(--green);
  }
  .brand {
    position: absolute; left: 0; top: 128px; width: 216px;
    text-align: center; font-family: var(--serif);
    font-size: 22px; color: var(--blue); line-height: 1.15;
  }
  .couple-photo {
    position: absolute; left: 0; top: 260px; width: 216px; height: 288px;
    background:
      radial-gradient(ellipse 42% 55% at 30% 62%, rgba(120,120,120,.55) 0%, rgba(120,120,120,0) 100%),
      radial-gradient(ellipse 40% 60% at 75% 55%, rgba(150,150,150,.5) 0%, rgba(150,150,150,0) 100%),
      linear-gradient(180deg, #ffffff 0%, #ececec 40%, #d2d2d2 100%);
  }
</style>
</head>
<body>
  <section class="banner">
    <div class="mist"></div>
    <div class="feather" role="img" aria-label="White feather floating"></div>
    <div class="stones" role="img" aria-label="Stacked zen stones in mist"></div>
    <div class="lotus" role="img" aria-label="Glowing lotus flower on water"></div>

    <div class="headline">
      <p class="l1"><span class="s">ARE YOU</span><span class="g">TROUBLE</span><span class="s">BY BEING</span></p>
      <p class="l2"><span class="b">OUT OF SHAPE</span><span class="s">AND WANTING</span></p>
      <p class="l3"><span class="s">TO GET BACK INTO THE SHAPE</span><span class="gl">QUICKLY?</span></p>
      <p class="l4"><span class="g">COME</span><span class="s">AND TRY OUR</span><span class="bm">SLIMMING MASSAGE</span></p>
      <p class="l5"><span class="s">ONLY AT</span><span class="price">$88</span><span class="s">DOLLAR,</span><span class="b">RESULTS GUARANTEE.</span></p>
      <p class="l6"><span class="terms">(TERMS AND CONDITIONS APPLIED)</span></p>
    </div>

    <div class="contact">
      <div class="address">24 Lagoon Crescent #02-17, Singapore - 430024</div>
      <div class="phone">+65 65550142</div>
      <div class="web">www.facebook/violetharborspa</div>
    </div>

    <div class="rule-green"></div>
    <div class="rule-blue"></div>

    <aside class="side-panel">
      <div class="brand-dot"></div>
      <div class="brand">VIOLET HARBOR<br>SPA</div>
      <div class="couple-photo" role="img" aria-label="Man and woman in white clothing meditating, black and white photo"></div>
    </aside>
  </section>
</body>
</html>
```